Kestrel Building Works Business Card and more!

We need a business card design for Kestrel Building Works Ltd, a respected building company that specialises in high quality designer homes.

We're after a sleek, clean, modern business card that incorporates our new logo (see attached) and colours, with black being the background.

We are Certified Trade Craftsmen and need to include their logo (see attached) on our cards, balancing but not taking over our logo.

Details to be included:

Warren Pike
Director

Phone: 0219462513
Email: kestrelbuild.nz@mailbox-example.nz
Website: www.kestrelbuildingworks.co.nz

Additional Information

A start up website is also under construction and needing attention and letterheads are needed!

We look forward to your designs!

Target Market(s)

30+ people who are interested in building new or renovating current homes

Industry/Entity Type

Construction

Contact Information for Business Card

Warren Pike
Director

Phone: 0219462513
Facebook: www.socialpage-example.com/kestrelbuild.nz

Font styles to use
Serif

Colors

Designer to choose colors to be used in the design.

Requirements
Must have
• Our new logo
• Our colours
• ctc logo

```html
<!DOCTYPE html>
<html lang="en">
<head>
<meta charset="utf-8">
<title>Kestrel Building Works – Business Card</title>
<link rel="stylesheet" href="https://fonts.googleapis.com/css2?family=Cinzel:wght@700&family=Roboto+Condensed:wght@500&family=Roboto:wght@400&display=swap">
<style>
  :root {
    --backdrop: #e7e4df;
    --card-light: #f5f2ed;
    --card-dark: #1f1d1b;
    --gold: #c79a62;
    --gold-soft: #d9b486;
    --ink: #262422;
    --contact-text: #e8dccb;
    --badge-fill: #d8c7b3;
  }
  * { margin: 0; padding: 0; box-sizing: border-box; }
  html, body {
    width: 1200px;
    height: 1054px;
    overflow: hidden;
    background: var(--backdrop);
  }
  .card {
    position: absolute;
    left: 100px;
    top: 227px;
    width: 1000px;
    height: 600px;
    background: var(--card-light);
    overflow: hidden;
    box-shadow: 0 18px 40px rgba(0,0,0,0.18);
  }
  .card-waves {
    position: absolute;
    inset: 0;
    width: 1000px;
    height: 600px;
  }
  .brand {
    position: absolute;
    left: 70px;
    top: 150px;
    width: 460px;
    text-align: center;
  }
  .brand-mark {
    display: block;
    width: 26px;
    height: 26px;
    margin: 0 auto 22px;
    background: var(--gold);
    border-radius: 50%;
  }
  .brand-name {
    font-family: "Cinzel", serif;
    font-weight: 700;
    font-size: 50px;
    line-height: 1.05;
    letter-spacing: 3px;
    color: var(--ink);
    text-transform: uppercase;
  }
  .person {
    position: absolute;
    right: 58px;
    top: 78px;
    text-align: right;
  }
  .person-name {
    font-family: "Roboto Condensed", sans-serif;
    font-weight: 500;
    font-size: 40px;
    color: var(--gold);
    line-height: 1.1;
  }
  .person-role {
    font-family: "Roboto", sans-serif;
    font-size: 25px;
    color: var(--ink);
    margin-top: 12px;
  }
  .contacts {
    position: absolute;
    right: 42px;
    top: 443px;
    list-style: none;
  }
  .contact-item {
    display: flex;
    justify-content: flex-end;
    align-items: center;
    height: 38px;
    font-family: "Roboto", sans-serif;
    font-size: 23px;
    color: var(--contact-text);
  }
  .contact-icon {
    width: 22px;
    height: 22px;
    margin-left: 22px;
    fill: var(--gold);
  }
  .badge {
    position: absolute;
    left: 59px;
    top: 411px;
    width: 166px;
    height: 166px;
  }
</style>
</head>
<body>
  <main class="card">
    <svg class="card-waves" viewBox="0 0 1000 600" aria-hidden="true">
      <path class="wave-band" fill="var(--gold)"
        d="M0 405 C 180 440, 330 420, 520 370 C 700 320, 860 300, 1000 297 L 1000 326 C 860 330, 700 350, 520 400 C 330 450, 180 470, 0 437 Z"/>
      <path class="wave-dark" fill="var(--card-dark)"
        d="M0 469 C 120 490, 220 495, 380 450 C 600 385, 820 320, 1000 326 L 1000 600 L 0 600 Z"/>
      <path class="wave-line" fill="none" stroke="var(--gold-soft)" stroke-width="5"
        d="M218 470 C 380 440, 560 370, 720 320 C 840 290, 930 283, 1000 284"/>
      <path class="wave-line" fill="none" stroke="var(--gold)" stroke-width="4"
        d="M230 520 C 400 500, 520 470, 640 430"/>
    </svg>

    <div class="brand">
      <span class="brand-mark"></span>
      <p class="brand-name">Kestrel<br>Building Works</p>
    </div>

    <div class="person">
      <p class="person-name">Warren Pike</p>
      <p class="person-role">Managing Director</p>
    </div>

    <svg class="badge" viewBox="0 0 166 166" role="img" aria-label="Certified Trade Craftsmen membership badge">
      <circle cx="83" cy="83" r="82" fill="var(--badge-fill)"/>
      <circle cx="83" cy="83" r="50" fill="var(--card-dark)"/>
    </svg>

    <ul class="contacts">
      <li class="contact-item">0219462513
        <svg class="contact-icon" viewBox="0 0 24 24" aria-hidden="true"><path d="M6.6 10.8c1.4 2.8 3.8 5.1 6.6 6.6l2.2-2.2c.3-.3.7-.4 1-.2 1.1.4 2.3.6 3.6.6.6 0 1 .4 1 1V20c0 .6-.4 1-1 1C10.6 21 3 13.4 3 4c0-.6.4-1 1-1h3.5c.6 0 1 .4 1 1 0 1.3.2 2.5.6 3.6.1.3 0 .7-.2 1z"/></svg>
      </li>
      <li class="contact-item">kestrelbuildingworks.co.nz
        <svg class="contact-icon" viewBox="0 0 24 24" aria-hidden="true"><path d="M2 5h20v14H2z M4 7v.4l8 5.2 8-5.2V7z" fill-rule="evenodd"/></svg>
      </li>
      <li class="contact-item">kestrelbuild.nz@mailbox-example.nz
        <svg class="contact-icon" viewBox="0 0 24 24" aria-hidden="true"><path fill-rule="evenodd" d="M12 2a10 10 0 1 0 0 20 10 10 0 0 0 0-20zm-1 2.1V11H7.1c.2-3 1.7-5.6 3.9-6.9zm2 0c2.2 1.3 3.7 3.9 3.9 6.9H13zM4.1 11a8 8 0 0 1 4.3-6.2C7.1 6.4 6.2 8.6 6.1 11zm11.5-6.2A8 8 0 0 1 19.9 11h-2c-.1-2.4-1-4.6-2.3-6.2zM4.1 13h2c.1 2.4 1 4.6 2.3 6.2A8 8 0 0 1 4.1 13zm3 0H11v6.9c-2.2-1.3-3.7-3.9-3.9-6.9zm5.9 0h3.9c-.2 3-1.7 5.6-3.9 6.9zm4.9 0h2a8 8 0 0 1-4.3 6.2c1.3-1.6 2.2-3.8 2.3-6.2z"/></svg>
      </li>
    </ul>
  </main>
</body>
</html>
```